Want a DL Flyer designed for mailout, with the following info. Please see the website www.ledgerwise.com.au for any other info.
Content:
EVERYTHING YOU NEED FROM AN ACCOUNTANT
(tick) Value for money
(tick) Mobile visits to your farm or business
(tick) Fixed Fees Agreed Upfront
(tick) Advice tailored to your circumstances
(tick) Help to grow your business
(tick) Talk directly to your accountant, the person who knows you
(tick) Small business & Primary Producer Specialists
+ MORE.......LEDGERWISE. YOU'RE MORE THAN A FILE TO US.
Director: Peter Dunmore CPA | Associate: Belinda Vasey CPA
Call (07) 4619 2235 www.ledgerwise.com.au PO Box 716 Kelvale Qld 4399

```html
<!DOCTYPE html>
<html lang="en">
<head>
<meta charset="utf-8">
<title>Ledgerwise DL Flyer</title>
<link rel="stylesheet" href="https://fonts.googleapis.com/css2?family=Arimo:wght@400;700&family=Tinos:wght@400&display=swap">
<style>
  :root {
    --red: #d71f26;
    --red-dark: #b5141b;
    --navy: #141b3c;
    --ink: #1a1a1a;
    --paper: #ffffff;
    --paper-grey: #eceef0;
    --stage: #d9dadc;
    --photo-blue: #5d8ea6;
    --photo-dark: #1f3d52;
    --office-light: #dfe7ee;
    --office-mid: #a9bccb;
  }
  * { margin: 0; padding: 0; box-sizing: border-box; }
  html, body { width: 1200px; height: 798px; overflow: hidden; }
  body {
    background: var(--stage);
    font-family: "Arimo", Arial, sans-serif;
    position: relative;
  }
  .flyer {
    position: absolute;
    left: 340px;
    top: 24px;
    width: 520px;
    height: 750px;
    background: linear-gradient(180deg, var(--paper) 0%, var(--paper-grey) 100%);
    overflow: hidden;
    box-shadow: 0 6px 18px rgba(0,0,0,0.18);
  }
  .flyer__shapes { position: absolute; inset: 0; }
  .collage-photo {
    position: absolute;
    left: 0; top: 0;
    width: 300px; height: 180px;
    clip-path: path("M0 0 H300 C250 60 190 130 0 176 Z");
    background: linear-gradient(135deg, var(--photo-dark) 0%, var(--photo-blue) 55%, #9fc3d2 100%);
  }
  .office-photo {
    position: absolute;
    left: 0; top: 222px;
    width: 520px; height: 268px;
    background: linear-gradient(100deg, var(--office-light) 0%, #f4f6f8 35%, var(--office-mid) 75%, #7f9fb8 100%);
  }
  .brand {
    position: absolute;
    right: 46px; top: 70px;
    display: flex; align-items: center; gap: 10px;
  }
  .brand__mark { width: 30px; height: 30px; background: var(--red); }
  .brand__name { color: var(--red); font-weight: 700; font-size: 30px; letter-spacing: -0.5px; }
  .headline-band {
    position: absolute;
    left: 0; top: 182px;
    width: 520px; height: 40px;
    background: linear-gradient(180deg, var(--red) 0%, var(--red-dark) 100%);
    color: var(--paper);
    font-weight: 700; font-size: 16px; letter-spacing: 0.6px;
    display: flex; align-items: center; justify-content: center;
  }
  .benefits {
    position: absolute;
    left: 36px; top: 250px;
    list-style: none;
  }
  .benefits li {
    position: relative;
    padding-left: 22px;
    margin-bottom: 14px;
    font-weight: 700; font-size: 15px;
    color: var(--ink);
    text-shadow: 0 0 4px #fff, 0 0 2px #fff;
  }
  .benefits li::before {
    content: "";
    position: absolute; left: 0; top: 5px;
    width: 8px; height: 8px; border-radius: 50%;
    background: var(--ink);
  }
  .firm-name {
    position: absolute;
    left: 0; right: 0; top: 500px;
    text-align: center;
    color: var(--red); font-weight: 700; font-size: 30px; letter-spacing: 1px;
  }
  .tagline {
    position: absolute;
    left: 0; right: 0; top: 540px;
    text-align: center;
    color: var(--navy); font-weight: 700; font-size: 20px; letter-spacing: 0.3px;
  }
  .team {
    position: absolute;
    left: 0; right: 0; top: 574px;
    text-align: center;
    color: var(--red); font-weight: 700; font-size: 12px; font-variant: small-caps; letter-spacing: 0.4px;
  }
  .contact {
    position: absolute;
    right: 50px; top: 654px;
    text-align: center;
    color: var(--paper);
    font-family: "Tinos", "Times New Roman", serif;
    font-style: normal;
    font-size: 17px; line-height: 1.35;
  }
</style>
</head>
<body>
  <main class="flyer">
    <div class="collage-photo" role="img" aria-label="Collage of business photos: a handshake and people in an office, in blue tones"></div>

    <svg class="flyer__shapes" width="520" height="750" viewBox="0 0 520 750" aria-hidden="true">
      <path d="M300 0 C250 60 190 130 0 176 L0 182 C200 136 262 62 318 0 Z" fill="#c9cdd2"/>
      <path d="M0 750 L0 722 C160 652 330 604 520 582 L520 750 Z" fill="var(--red)"/>
      <path d="M0 722 C160 652 330 604 520 582 L520 594 C340 616 170 664 0 734 Z" fill="var(--red-dark)"/>
    </svg>

    <div class="brand">
      <span class="brand__mark"></span>
      <span class="brand__name">Ledgerwise</span>
    </div>

    <div class="headline-band">EVERYTHING YOU NEED FROM AN ACCOUNTANT</div>

    <div class="office-photo" role="img" aria-label="Photo of two women working together over paperwork and a laptop at an office desk"></div>

    <ul class="benefits">
      <li>Value for money</li>
      <li>Mobile visits to your farm or business</li>
      <li>Fixed Fees Agreed Upfront</li>
      <li>Advice tailored to your circumstances</li>
      <li>Help to grow your business</li>
      <li>Talk directly to your accountant, the person who knows you</li>
      <li>Small business &amp; Primary Producer Specialists</li>
    </ul>

    <p class="firm-name">LEDGERWISE</p>
    <p class="tagline">YOU'RE MORE THAN A FILE TO US.</p>
    <p class="team">Director: Peter Dunmore CPA | Associate: Belinda Vasey CPA</p>

    <address class="contact">
      Call (07) 4619 2235<br>
      www.ledgerwise.com.au<br>
      PO Box 716 Kelvale Qld 4399
    </address>
  </main>
</body>
</html>
```